Chai Tea Company needs a Tea Packaging Box Design

Tea Packaging
Dimensions of the Tea Packaging Box: Height 13 cm; Width 8.5 cm; Depth 7 cm
Individual Teabag Packet/ Sachet: Width 6.5 cm; Length 8.25 cm
We are looking for a new tea packaging design, for our tea business. The material of the box is cardboard. We are also looking for a design that will be on each individual tea bag sachet/packet that goes into the box. This design will be very similar to what you design for the tea packaging box.
Product Info:
Our tea company is called “Velmora Leaf”. We sell two types of Chai Tea, once called “Velmora Gold” and one called “Velmora Bloom”. The Velmora Gold has caffeine, while the Velmora Bloom is Naturally Caffeine Free. The Velmora Gold has a black tea base, while the Velmora Bloom has a Rooibos tea base. We will need two tea packaging designs, one for each Chai Tea flavour. The designs for both the teas can be similar, but make sure that you can easily distinguish one from the other (example: make them have different colours or pictures). Both the chai teas, come from the same product line.
Tea Packaging Design:
We are looking for high end tea packaging. We produce high quality teas, and we would like to portray this in our tea packaging. Our teas are made with no artificial flavourings, natural flavourings, or preservatives, so we would also like a natural, organic, high quality look to our tea packaging. Our current logo is a llama. It would be great if you could make the current logo more polished and well made. If you feel that the llama is not well suited or you would like to design the llama differently, we are open to your creative ideas.
General Basic Info:
Keep in mind, we will have both English and French writing on the tea packaging. You do not need to worry about the French writing (we will do the translation), just make sure there is room for it. However, if you feel that you are capable and knowledgeable of incorporating both French and English language into the tea packaging that would be of great help and value.
Back of the Box:
- Will have ingredients and brewing instructions. Basic brewing instructions are: “Add hot water to teabag. Steep for 5-7 minutes, depending on strength preferred. Add milk and your choice of sweetener. Enjoy! See inside panel of box for more detailed instructions”. (The basic brewing instructions, can further be polished or written in a more creative or professional manner).
Front of the Box:
- Will have company name, type of tea, little description of the tea
- 18 teabags
- 54 g (1.9 OZ)
- Should state that this is a product of Alberta, Canada.
Side of the Box:
Any creative wording, slogan, or description about the tea, or whatever you feel would be good on the side of the box.
On the inside flap of the side of the box, there will be detailed instructions on how to brew the tea. These will be different from the simplified brewing instructions on the back of the box. I have attached the advanced brewing instructions as a file. These instructions can further be simplified or reduced to make it easier and cleaner for the consumers to read.
Individual Tea Sachets/ Packets
- These will have a matching look and design of the tea box packaging, except on a smaller scale. Each individual sachet will have the company name, type of tea, little description of the tea in the front of the sachet, while the back will contain the ingredients, and basic brewing instructions.
I have attached a few files, with the dimensions, ingredients, detailed brewing directions, and current logo of the business.
If you have any questions, about the design or packaging please let me know. The winning designer will be required to do a few additional tweaks to finalize the product. Thank you for your time and happy designing!

```html
<!DOCTYPE html>
<html lang="en">
<head>
<meta charset="utf-8">
<title>Velmora Bloom – Tea Packaging</title>
<link href="https://fonts.googleapis.com/css2?family=Alegreya:wght@400;700&family=Merienda:wght@700&family=Signika:wght@400;600;700&display=swap" rel="stylesheet">
<style>
  :root {
    --backdrop: #262523;
    --leaf-green: #2f5e22;
    --deep-green: #24491a;
    --paper: #eeebdf;
    --medallion: #fbfaf4;
    --flap-white: #f7f7f5;
    --badge-dark: #2b2b22;
    --ink-white: #ffffff;
    --placeholder: #d9ddd2;
  }
  html, body {
    margin: 0;
    width: 1200px;
    height: 900px;
    overflow: hidden;
    background: var(--backdrop);
  }
  .canvas { display: block; width: 1200px; height: 900px; }

  .brand-name { font-family: "Signika", sans-serif; font-weight: 700; fill: var(--leaf-green); }
  .brand-name--light { fill: var(--ink-white); }
  .product-name { font-family: "Merienda", cursive; font-weight: 700; fill: var(--leaf-green); }
  .product-name--light { fill: var(--ink-white); }
  .body-copy { font-family: "Alegreya", serif; fill: var(--deep-green); }
  .body-copy--light { fill: var(--ink-white); }
  .body-copy--bold { font-weight: 700; }
  .caption { font-family: "Signika", sans-serif; fill: var(--deep-green); }
  .caption--light { fill: var(--ink-white); }

  .paper { fill: var(--paper); }
  .green-band { fill: var(--leaf-green); }
  .medallion { fill: var(--medallion); }
  .medallion-ring { fill: none; stroke: var(--leaf-green); stroke-width: 1.6; stroke-dasharray: 1.5 3.5; stroke-linecap: round; }
  .rule { stroke: var(--leaf-green); stroke-width: 1.2; }
  .rule--light { stroke: var(--ink-white); stroke-width: 0.8; }
  .brand-dot { fill: none; stroke: var(--leaf-green); stroke-width: 1.4; }
  .count-badge { fill: var(--badge-dark); stroke: var(--ink-white); stroke-width: 1.2; }
  .glue-tab { fill: var(--flap-white); }
  .name-strip { fill: var(--paper); }
  .leaf-bullet { fill: var(--leaf-green); }
  .illustration-slot { fill: var(--placeholder); }
</style>
</head>
<body>
<svg class="canvas" viewBox="0 0 1200 900" xmlns="http://www.w3.org/2000/svg" xmlns:xlink="http://www.w3.org/1999/xlink">
  <defs>
    <!-- Front panel of the box -->
    <symbol id="front-panel" viewBox="0 0 250 410">
      <path id="front-arc" d="M 38 210 A 87 87 0 0 1 212 210" fill="none"/>
      <rect class="paper" x="0" y="0" width="250" height="410"/>
      <rect class="green-band" x="0" y="0" width="250" height="110"/>
      <rect class="green-band" x="0" y="315" width="250" height="95"/>
      <circle class="medallion" cx="125" cy="205" r="118"/>
      <circle class="medallion-ring" cx="125" cy="205" r="111"/>
      <text class="brand-name" font-size="21" text-anchor="middle">
        <textPath href="#front-arc" startOffset="50%">Velmora Leaf</textPath>
      </text>
      <circle class="brand-dot" cx="125" cy="152" r="10"/>
      <line class="rule" x1="48" y1="172" x2="202" y2="172"/>
      <text class="product-name" x="125" y="199" font-size="23" text-anchor="middle">Velmora Bloom</text>
      <line class="rule" x1="48" y1="210" x2="202" y2="210"/>
      <text class="body-copy" font-size="9.5" text-anchor="middle">
        <tspan x="125" y="228">CHAI is a rich blend of strong and flavourful tea,</tspan>
        <tspan x="125" y="240">aromatic spices, milk and sugar.</tspan>
        <tspan x="125" y="256" font-size="8">• • •</tspan>
        <tspan x="125" y="271">CHAI est un riche mélange de thé fort</tspan>
        <tspan x="125" y="283">et savoureux, aromates,</tspan>
        <tspan x="125" y="295">le lait et le sucre.</tspan>
      </text>
      <text class="caption caption--light" font-size="11">
        <tspan x="12" y="368">54 g</tspan>
        <tspan x="12" y="384">1.9 OZ</tspan>
      </text>
      <text class="body-copy body-copy--light" font-size="11.5">
        <tspan x="58" y="360">Product of Alberta, Canada</tspan>
        <tspan x="58" y="386">Produit de l'Alberta, Canada</tspan>
      </text>
      <line class="rule--light" x1="58" y1="370" x2="185" y2="370"/>
      <circle class="count-badge" cx="220" cy="372" r="23"/>
      <text class="caption caption--light" x="220" y="379" font-size="19" font-weight="700" text-anchor="middle">18</text>
      <text class="caption caption--light" x="220" y="360" font-size="6" text-anchor="middle">teabags</text>
      <text class="caption caption--light" x="220" y="389" font-size="5.5" text-anchor="middle">sachets de thé</text>
    </symbol>

    <!-- Side panel of the box -->
    <symbol id="side-panel" viewBox="0 0 115 287">
      <rect class="paper" x="0" y="0" width="115" height="287"/>
      <rect class="green-band" x="18" y="0" width="79" height="287"/>
      <text class="brand-name brand-name--light" x="57.5" y="20" font-size="8.5" text-anchor="middle">Velmora Leaf</text>
      <text class="body-copy body-copy--light" font-size="7" text-anchor="middle">
        <tspan x="57.5" y="38">CHAI is a rich blend</tspan>
        <tspan x="57.5" y="47">of strong and flavourful tea,</tspan>
        <tspan x="57.5" y="56">aromatic spices,</tspan>
        <tspan x="57.5" y="65">milk and sugar.</tspan>
        <tspan x="57.5" y="74">Authentic Chai is an art</tspan>
        <tspan x="57.5" y="83">that requires</tspan>
        <tspan x="57.5" y="92">all natural ingredients,</tspan>
        <tspan x="57.5" y="101">care and time to prepare.</tspan>
      </text>
      <rect class="name-strip" x="18" y="116" width="79" height="24"/>
      <text class="product-name" x="57.5" y="132" font-size="10" text-anchor="middle" textLength="72" lengthAdjust="spacingAndGlyphs">Velmora Bloom</text>
      <text class="body-copy body-copy--light" font-size="7" text-anchor="middle">
        <tspan x="57.5" y="158">CHAI est un riche mélange</tspan>
        <tspan x="57.5" y="167">de thé fort et savoureux,</tspan>
        <tspan x="57.5" y="176">aromates, le lait et le sucre.</tspan>
        <tspan x="57.5" y="185">Authentique Chai est</tspan>
        <tspan x="57.5" y="194">un art qui exige</tspan>
        <tspan x="57.5" y="203">tout naturel ingrédients,</tspan>
        <tspan x="57.5" y="212">de soins et de temps</tspan>
        <tspan x="57.5" y="221">pour préparer.</tspan>
      </text>
      <circle class="count-badge" cx="57.5" cy="262" r="12"/>
      <text class="caption caption--light" x="57.5" y="266" font-size="10" font-weight="700" text-anchor="middle">18</text>
    </symbol>
  </defs>

  <!-- Flat front panel -->
  <g class="box-front">
    <use href="#front-panel" x="140" y="60" width="275" height="451"/>
  </g>

  <!-- Teabag sachet, front -->
  <g class="sachet-front" transform="translate(110 560)">
    <path id="sachet-arc" d="M 27 112 A 55 55 0 0 1 137 112" fill="none"/>
    <rect class="paper" width="165" height="210"/>
    <rect class="green-band" x="22" y="0" width="121" height="52"/>
    <circle class="medallion" cx="82.5" cy="112" r="70"/>
    <circle class="medallion-ring" cx="82.5" cy="112" r="65"/>
    <text class="brand-name" font-size="13" text-anchor="middle">
      <textPath href="#sachet-arc" startOffset="50%">Velmora Leaf</textPath>
    </text>
    <circle class="brand-dot" cx="82.5" cy="80" r="6"/>
    <line class="rule" x1="35" y1="92" x2="130" y2="92"/>
    <text class="product-name" x="82.5" y="110" font-size="14" text-anchor="middle">Velmora Bloom</text>
    <line class="rule" x1="35" y1="117" x2="130" y2="117"/>
    <text class="body-copy" font-size="5.2" text-anchor="middle">
      <tspan x="82.5" y="127">CHAI is a rich blend of strong and flavourful tea, aromatic spices,</tspan>
      <tspan x="82.5" y="134">milk and sugar. Authentic Chai is an art that requires</tspan>
      <tspan x="82.5" y="141">all natural ingredients, care and time to prepare.</tspan>
      <tspan x="82.5" y="150">CHAI est un riche mélange de thé fort et savoureux,</tspan>
      <tspan x="82.5" y="157">aromates, le lait et le sucre. Authentique Chai est</tspan>
      <tspan x="82.5" y="164">un art qui exige tout naturel ingrédients,</tspan>
      <tspan x="82.5" y="171">de soins et de temps pour préparer.</tspan>
    </text>
  </g>

  <!-- Teabag sachet, back -->
  <g class="sachet-back" transform="translate(300 560)">
    <rect class="paper" width="162" height="210"/>
    <text class="caption" x="26" y="16" font-size="8.5" font-weight="700">INGREDIENTS /for 2 cups/:</text>
    <g class="ingredient-list">
      <ellipse class="leaf-bullet" cx="17" cy="26" rx="3.5" ry="2.2"/>
      <ellipse class="leaf-bullet" cx="17" cy="37" rx="3.5" ry="2.2"/>
      <ellipse class="leaf-bullet" cx="17" cy="48" rx="3.5" ry="2.2"/>
      <ellipse class="leaf-bullet" cx="17" cy="59" rx="3.5" ry="2.2"/>
      <ellipse class="leaf-bullet" cx="17" cy="79" rx="3.5" ry="2.2"/>
      <text class="body-copy" font-size="7.2">
        <tspan x="26" y="29">1½ cups (12 oz) water.</tspan>
        <tspan x="26" y="40">2 Chai tea bags.</tspan>
        <tspan x="26" y="51">1 cup (8oz) (whole) milk.</tspan>
        <tspan x="26" y="62">2-4 teaspoons sugar</tspan>
        <tspan x="26" y="71">or honey to taste</tspan>
        <tspan x="26" y="82">1-2 teaspoons of sliced</tspan>
        <tspan x="26" y="91">or grated fresh ginger (optional)</tspan>
      </text>
    </g>
    <text class="caption" x="26" y="112" font-size="8.5" font-weight="700">INGRÉDIENTS /pour 2 tasses/:</text>
    <g class="ingredient-list">
      <ellipse class="leaf-bullet" cx="17" cy="122" rx="3.5" ry="2.2"/>
      <ellipse class="leaf-bullet" cx="17" cy="133" rx="3.5" ry="2.2"/>
      <ellipse class="leaf-bullet" cx="17" cy="144" rx="3.5" ry="2.2"/>
      <ellipse class="leaf-bullet" cx="17" cy="155" rx="3.5" ry="2.2"/>
      <ellipse class="leaf-bullet" cx="17" cy="175" rx="3.5" ry="2.2"/>
      <text class="body-copy" font-size="7.2">
        <tspan x="26" y="125">1½ tasse (12 oz) d'eau.</tspan>
        <tspan x="26" y="136">2 sachets de thé Chai.</tspan>
        <tspan x="26" y="147">1 tasse (8 onces) (ensemble) lait.</tspan>
        <tspan x="26" y="158">2-4 cuillères à café de sucre ou</tspan>
        <tspan x="26" y="167">de miel au goût</tspan>
        <tspan x="26" y="178">1-2 cuillères à café de gingembre</tspan>
        <tspan x="26" y="187">frais tranchés ou râpé (facultatif)</tspan>
      </text>
    </g>
  </g>

  <!-- Box dieline -->
  <g class="dieline">
    <!-- top tuck flap and dust flaps -->
    <path class="glue-tab" d="M770 60 Q770 48 782 48 L830 48 L830 180 L770 180 Z"/>
    <path class="glue-tab" d="M1005 48 L1050 48 Q1062 48 1062 60 L1062 180 L1005 180 Z"/>
    <rect class="green-band" x="830" y="20" width="175" height="165"/>

    <!-- inner flap with brewing steps (reads upside down) -->
    <g class="inner-flap" transform="translate(830 185)">
      <rect class="paper" width="175" height="255"/>
      <g transform="rotate(180 87.5 127.5)">
        <path id="flap-arc" d="M 37 60 A 50 50 0 0 1 138 60" fill="none"/>
        <text class="brand-name" font-size="13" text-anchor="middle">
          <textPath href="#flap-arc" startOffset="50%">Velmora Leaf</textPath>
        </text>
        <text class="product-name" x="87.5" y="78" font-size="16" text-anchor="middle">Velmora Bloom</text>
        <g role="img" aria-label="Three line drawings of a cup: hot water poured over a teabag, the tea steeping, milk being added">
          <rect class="illustration-slot" x="14" y="94" width="44" height="50" rx="6"/>
          <rect class="illustration-slot" x="65" y="94" width="44" height="50" rx="6"/>
          <rect class="illustration-slot" x="116" y="94" width="44" height="50" rx="6"/>
        </g>
        <text class="body-copy" font-size="5.6" text-anchor="middle">
          <tspan x="36" y="158">Add hot water</tspan>
          <tspan x="36" y="165">to teabag.</tspan>
          <tspan x="87" y="158">Steep 5-7</tspan>
          <tspan x="87" y="165">minutes to taste.</tspan>
          <tspan x="138" y="158">Add milk and</tspan>
          <tspan x="138" y="165">sweetener. Enjoy!</tspan>
        </text>
        <text class="body-copy" x="87.5" y="200" font-size="6" text-anchor="middle">See inside panel of box for more detailed instructions</text>
        <text class="caption" font-size="8" text-anchor="middle">
          <tspan x="48" y="238">54 g</tspan>
          <tspan x="128" y="238">1.9 OZ</tspan>
        </text>
        <circle class="count-badge" cx="87.5" cy="235" r="10"/>
        <text class="caption caption--light" x="87.5" y="239" font-size="9" font-weight="700" text-anchor="middle">18</text>
      </g>
    </g>

    <!-- bottom tuck flap and dust flaps -->
    <path class="glue-tab" d="M770 464 Q770 452 782 452 L830 452 L830 580 L770 580 Z"/>
    <path class="glue-tab" d="M1005 452 L1050 452 Q1062 452 1062 464 L1062 580 L1005 580 Z"/>
    <rect class="green-band" x="830" y="450" width="175" height="138"/>
    <text class="brand-name brand-name--light" x="917.5" y="504" font-size="11" text-anchor="middle">Velmora Leaf</text>
    <text class="product-name product-name--light" x="917.5" y="528" font-size="16" text-anchor="middle">Velmora Bloom</text>

    <!-- main wrap: glue tab, side, front, side, tab -->
    <path class="glue-tab" d="M674 588 L715 588 L715 875 L674 875 Q662 875 662 863 L662 600 Q662 588 674 588 Z"/>
    <use href="#side-panel" x="715" y="588" width="115" height="287"/>
    <use href="#front-panel" x="830" y="588" width="175" height="287"/>
    <use href="#side-panel" x="1005" y="588" width="125" height="287" preserveAspectRatio="none"/>
    <path class="glue-tab" d="M1130 588 L1160 588 Q1172 588 1172 600 L1172 863 Q1172 875 1160 875 L1130 875 Z"/>

    <!-- bottom closure tabs -->
    <rect class="glue-tab" x="725" y="875" width="95" height="22"/>
    <rect class="glue-tab" x="840" y="875" width="155" height="22"/>
    <rect class="glue-tab" x="1015" y="875" width="105" height="22"/>
  </g>
</svg>
</body>
</html>
```